Brightvale Fluid Systems Corp Business Cards

Business cards to match the logo.

Company is a start up water technology company that has developed a patented system using centrifugal force to separate waste from municipal waste water to produce crystal clear clean water. Product sell starting at 2 million to governments both in the US and international.

Business cards should have a professional look with the target generally engineers.

Target Market(s)

Engineers, Government officials and investors

Industry/Entity Type

Water Treatment

Contact Information for Business Card

Business cards design will be used for 6 to 8 people with job titles. Can use the quote "If there is magic in the planet, it is contained in water." but not required to use quote. Should follow theme of Logo

Font styles to use
Other font styles liked:
• match logo font

Requirements
Nice to have
• Colors to match Logo. Business cards to match style of flow of Logo.
• Emphasis on clean look not a busy look. Clean flowing water.
Should not have
• Pictures of industrial equipment or wastewater

```html
<!DOCTYPE html>
<html lang="en">
<head>
<meta charset="UTF-8">
<title>Brightvale Fluid Systems Corp Business Cards</title>
<link href="https://fonts.googleapis.com/css2?family=Libre+Baskerville:wght@400;700&display=swap" rel="stylesheet">
<style>
  :root {
    --backdrop: #d9dadc;
    --card: #ffffff;
    --ink: #1b4f7c;
    --deep-blue: #155a8a;
    --sky-blue: #2aa7df;
    --on-band: #ffffff;
  }
  * { box-sizing: border-box; margin: 0; padding: 0; }
  html, body {
    width: 1200px;
    height: 900px;
    overflow: hidden;
  }
  body {
    background: var(--backdrop);
    font-family: "Libre Baskerville", Georgia, serif;
    color: var(--ink);
    display: flex;
    flex-direction: column;
    align-items: center;
    justify-content: center;
    gap: 40px;
  }
  .business-card {
    position: relative;
    width: 700px;
    height: 400px;
    background: var(--card);
    box-shadow: 0 6px 18px rgba(0, 0, 0, 0.18);
    overflow: hidden;
  }
  .water-band {
    position: absolute;
    left: 0;
    right: 0;
    bottom: 0;
    background: linear-gradient(180deg, var(--sky-blue) 0%, var(--deep-blue) 45%, var(--deep-blue) 100%);
  }
  .card-back .water-band { height: 120px; }
  .card-front .water-band { height: 100px; }

  /* Back side: person and contact details */
  .holder {
    position: absolute;
    left: 48px;
    top: 58px;
    text-transform: uppercase;
    font-weight: 700;
    line-height: 1.25;
  }
  .holder-name { font-size: 20px; letter-spacing: 0.5px; }
  .holder-title { font-size: 17px; padding-left: 8px; }

  .contact-list {
    position: absolute;
    left: 400px;
    top: 76px;
    list-style: none;
    font-size: 14px;
    line-height: 1;
  }
  .contact-item {
    display: flex;
    align-items: center;
    gap: 10px;
    margin-bottom: 10px;
  }
  .contact-icon {
    width: 14px;
    height: 14px;
    fill: var(--ink);
    flex: none;
  }
  .website {
    position: absolute;
    left: 0;
    right: 0;
    bottom: 30px;
    text-align: center;
    color: var(--on-band);
    font-size: 15px;
    font-weight: 700;
    letter-spacing: 0.5px;
  }

  /* Front side: company name */
  .company-name {
    position: absolute;
    left: 0;
    right: 0;
    top: 100px;
    text-align: center;
    font-size: 40px;
    font-weight: 700;
    color: var(--deep-blue);
    letter-spacing: 1px;
    text-transform: uppercase;
    line-height: 1.15;
  }
</style>
</head>
<body>

  <section class="business-card card-back" aria-label="Card back with contact details">
    <div class="water-band" role="img" aria-label="Flowing water wave artwork in light and deep blue"></div>

    <div class="holder">
      <p class="holder-name">Your Name Here</p>
      <p class="holder-title">Your Title Here</p>
    </div>

    <ul class="contact-list">
      <li class="contact-item">
        <svg class="contact-icon" viewBox="0 0 24 24" aria-hidden="true"><path d="M12 2a7 7 0 0 0-7 7c0 5 7 13 7 13s7-8 7-13a7 7 0 0 0-7-7zm0 9.5A2.5 2.5 0 1 1 12 6.5a2.5 2.5 0 0 1 0 5z"/></svg>
        <span>Company address here</span>
      </li>
      <li class="contact-item">
        <svg class="contact-icon" viewBox="0 0 24 24" aria-hidden="true"><path d="M6.6 10.8a15 15 0 0 0 6.6 6.6l2.2-2.2a1 1 0 0 1 1-.25 11.4 11.4 0 0 0 3.6.57 1 1 0 0 1 1 1V20a1 1 0 0 1-1 1A17 17 0 0 1 3 4a1 1 0 0 1 1-1h3.5a1 1 0 0 1 1 1c0 1.25.2 2.45.57 3.57a1 1 0 0 1-.25 1z"/></svg>
        <span>Company phone number</span>
      </li>
      <li class="contact-item">
        <svg class="contact-icon" viewBox="0 0 24 24" aria-hidden="true"><path d="M7 1h10a2 2 0 0 1 2 2v18a2 2 0 0 1-2 2H7a2 2 0 0 1-2-2V3a2 2 0 0 1 2-2zm0 3v14h10V4zm5 15.5a1.2 1.2 0 1 0 0 2.4 1.2 1.2 0 0 0 0-2.4z"/></svg>
        <span>Cell phone number</span>
      </li>
      <li class="contact-item">
        <svg class="contact-icon" viewBox="0 0 24 24" aria-hidden="true"><path d="M2 5h20v14H2zm2 2v.5l8 5 8-5V7zm0 2.8V17h16V9.8l-8 5z"/></svg>
        <span>e-mail address</span>
      </li>
    </ul>

    <p class="website">Website address here</p>
  </section>

  <section class="business-card card-front" aria-label="Card front with company name">
    <div class="water-band" role="img" aria-label="Flowing water wave artwork in light and deep blue"></div>

    <h1 class="company-name">Brightvale<br>Fluid Systems</h1>
  </section>

</body>
</html>
```